Bref créative
Retro design logo for building Materials company
R.K. Morrow Company
Professional
Peter K. Morrow IV
LEED AP BD+C
342 Ferngate Lane, Suite B
Hot Springs, AR 72814
pmorrow@rkmorrowsupply.com
This is my logo AI file.

```html
<!DOCTYPE html>
<html lang="en">
<head>
<meta charset="utf-8">
<title>R.K. Morrow Company — Business Card</title>
<link href="https://fonts.googleapis.com/css2?family=Cinzel:wght@400&family=Lato:wght@300;400&display=swap" rel="stylesheet">
<style>
  :root {
    --backdrop: #e4e4e2;
    --card: #121212;
    --card-edge: #1c1c1c;
    --ink: #f2f2f2;
    --ink-soft: #b9b9b9;
  }
  * { box-sizing: border-box; margin: 0; padding: 0; }
  html, body {
    width: 1200px; height: 901px; overflow: hidden;
    background: var(--backdrop);
  }
  .stage {
    width: 1200px; height: 901px;
    display: flex; align-items: center; justify-content: center; gap: 44px;
  }
  .card {
    position: relative;
    width: 540px; height: 309px;
    background: linear-gradient(135deg, var(--card-edge), var(--card) 55%);
    border-radius: 6px;
    box-shadow: 0 10px 28px rgba(0,0,0,.25);
    color: var(--ink);
  }
  .brand {
    position: absolute; left: 28px; top: 78px; width: 250px;
    display: flex; flex-direction: column; align-items: center; gap: 22px;
  }
  .brand-mark {
    width: 84px; height: 84px; border-radius: 50%;
    border: 4px solid var(--ink);
  }
  .brand-name {
    font-family: "Cinzel", serif; font-size: 20px; letter-spacing: .1em;
    color: var(--ink); white-space: nowrap;
  }
  .contact {
    position: absolute; left: 304px; top: 44px; width: 216px;
    font-family: "Lato", sans-serif; font-weight: 300;
  }
  .contact-name {
    font-family: "Cinzel", serif; font-size: 15px; letter-spacing: .06em;
    white-space: nowrap;
  }
  .contact-title {
    font-size: 9px; letter-spacing: .14em; color: var(--ink-soft); margin-top: 3px;
  }
  .contact-list { list-style: none; margin-top: 26px; }
  .contact-item {
    display: flex; gap: 8px; align-items: flex-start;
    font-size: 9.5px; line-height: 1.45; color: var(--ink-soft); margin-bottom: 14px;
  }
  .contact-item svg { flex: none; width: 10px; height: 10px; margin-top: 2px; fill: var(--ink); }
  .card-back .brand-back {
    position: absolute; right: 40px; top: 50%; transform: translateY(-50%);
    display: flex; align-items: center; gap: 12px;
  }
  .brand-back .brand-mark { width: 52px; height: 52px; border-width: 3px; }
  .brand-back .brand-name { font-size: 14px; }
</style>
</head>
<body>
<main class="stage">
  <section class="card card-front">
    <div class="brand">
      <div class="brand-mark"></div>
      <div class="brand-name">R.K. MORROW Co.</div>
    </div>
    <div class="contact">
      <p class="contact-name">Peter K. Morrow IV</p>
      <p class="contact-title">LEED AP BD+C</p>
      <ul class="contact-list">
        <li class="contact-item">
          <svg viewBox="0 0 10 10"><path d="M5 0a3.5 3.5 0 0 0-3.5 3.5C1.5 6 5 10 5 10s3.5-4 3.5-6.5A3.5 3.5 0 0 0 5 0zm0 5a1.5 1.5 0 1 1 0-3 1.5 1.5 0 0 1 0 3z"/></svg>
          <span>342 Ferngate Lane, Suite B<br>Hot Springs, AR 72814</span>
        </li>
        <li class="contact-item">
          <svg viewBox="0 0 10 10"><path d="M2 0l2 2.5-1 1.2c.6 1.3 1.6 2.3 2.9 2.9L7 5.6 10 7.5 9 9.6C4.5 9.8.2 5.5.4 1z"/></svg>
          <span>501.555.0142</span>
        </li>
        <li class="contact-item">
          <svg viewBox="0 0 10 10"><path d="M0 2h10v6H0zm1 .8v.4L5 6l4-2.8v-.4L5 5.6z"/></svg>
          <span>pmorrow@rkmorrowsupply.com</span>
        </li>
      </ul>
    </div>
  </section>
  <section class="card card-back">
    <div class="brand-back">
      <div class="brand-mark"></div>
      <div class="brand-name">R.K. MORROW Co.</div>
    </div>
  </section>
</main>
</body>
</html>
```